Last Minute Accommodation Booking Portal

AlpenGlowDeals.com needs a web platform to put potential clients in touch with available local ski resort accommodation. We are a dynamic, friendly and versatile company; we like a clean, graphic, contemporary look!

Hotel and apartment owners offer rooms to rent for certain dates with pricing; clients can ask for specific dates and number of beds with their budget. Offers can see searchers requests, searchers can only see offers.

All dates requested and offered must be within two weeks of the posting date and then posts should be removed when their arrival date has passed or they can be deleted by the person posting. We are envisaging that the hotels/apartments and customers would each need to register and login their offer/request.

Target Market(s)

28-55 years, active, high net worth but like a bargain, last mintue deciders, skiers and snowboarders or mountain enthusiasts, city folk wanting a winter break

Industry/Entity Type

Accommodation

Coding

Number of Pages Required

Font styles to use
Sans Serif

Colors
cee9f5
33a6d7
e34297
b768aa
ffffff

Requirements
Must have
• Efficient functionality so that many different parties - both offering deals and searching for deals - can search/list at the same time.
• option to translate to french
Nice to have
• opt in to 'alert/notification' when new offer or search is listed

```html
<!DOCTYPE html>
<html lang="en">
<head>
<meta charset="utf-8">
<title>AlpenGlow Deals – Last Minute Accommodation Booking Portal</title>
<link href="https://fonts.googleapis.com/css2?family=Open+Sans:wght@400;600;700&family=Raleway:wght@500;600;700&display=swap" rel="stylesheet">
<style>
:root{
  --orange:#f7931e;
  --orange-dark:#e07f0c;
  --teal:#2fa6bd;
  --teal-soft:rgba(47,166,189,.88);
  --blue:#2c8fd3;
  --ink:#3a3f44;
  --muted:#7b8288;
  --white:#ffffff;
  --snow:#e9eef2;
  --footer:#1f4d52;
  --footer-deep:#163a3e;
  --line:#dfe4e8;
}
*{box-sizing:border-box;margin:0;padding:0}
html,body{width:768px;height:1200px;overflow:hidden}
body{font-family:"Open Sans",Arial,sans-serif;color:var(--ink);background:var(--white);position:relative}
.heading{font-family:"Raleway","Open Sans",sans-serif}

/* header */
.site-header{height:77px;display:flex;justify-content:space-between;align-items:center;padding:0 98px}
.brand{font-family:"Raleway",sans-serif;font-weight:700;font-size:24px;color:var(--orange);display:flex;align-items:center;gap:8px}
.brand-dot{width:12px;height:12px;border-radius:50%;background:var(--teal)}
.booking-contact{text-align:right}
.booking-contact .label{font-size:9px;font-weight:700;color:var(--orange);letter-spacing:.5px}
.booking-contact .phone{font-size:17px;font-weight:700;color:var(--ink);display:flex;align-items:center;gap:5px}

.main-nav{height:20px;background:var(--orange);display:flex;gap:28px;padding-left:98px;align-items:center}
.main-nav a{color:var(--white);font-size:9px;font-weight:700;text-decoration:none;letter-spacing:.4px}

/* hero */
.hero{position:relative;height:283px;background:linear-gradient(160deg,#9fb8c9 0%,#d9e3ea 35%,#7a5a44 60%,#4a3a30 100%)}
.hero-tagline{position:absolute;left:98px;top:90px;width:268px;background:var(--teal-soft);padding:14px 18px;color:var(--white)}
.hero-tagline h1{font-family:"Raleway",sans-serif;font-weight:600;font-size:19px;line-height:1.2}
.hero-tagline h2{font-family:"Raleway",sans-serif;font-weight:600;font-size:27px;line-height:1.1;margin-bottom:5px}
.hero-tagline p{font-size:8.5px;line-height:1.35}

.booking-form{position:absolute;right:98px;top:36px;width:180px;background:rgba(30,40,48,.72)}
.booking-form .title{background:var(--teal);color:var(--white);font-family:"Raleway",sans-serif;font-weight:700;font-size:14px;padding:7px 12px}
.booking-form .body{padding:8px 12px 12px}
.field-label{font-size:8.5px;color:var(--white);margin:4px 0 3px}
.field{height:17px;background:var(--white);font-size:8px;color:var(--muted);display:flex;align-items:center;padding:0 5px;gap:4px}
.selects{display:flex;gap:8px}
.selects div{flex:1}
.check-btn{margin-top:11px;height:22px;background:var(--orange);color:var(--white);font-size:9.5px;font-weight:700;display:flex;align-items:center;justify-content:center;letter-spacing:.4px}

/* welcome */
.welcome{text-align:center;padding:22px 98px 0}
.welcome h3{font-size:23px;font-weight:600;color:var(--ink);margin-bottom:14px}
.welcome p{font-size:8px;line-height:1.55;color:var(--muted);margin-bottom:10px}
.btn{display:inline-block;background:var(--blue);color:var(--white);font-size:8.5px;font-weight:600;padding:5px 13px}
.btn-row{display:flex;justify-content:center;gap:10px;margin-top:4px}

/* features */
.features{position:absolute;top:583px;left:0;width:768px;height:197px;background:linear-gradient(180deg,#f4f7f9,#dfe7ed);display:flex;gap:26px;padding:11px 98px 0}
.feature{flex:1}
.feature-photo{height:92px}
.feature h4{font-family:"Raleway",sans-serif;font-size:14px;font-weight:700;color:var(--orange);margin:10px 0 4px}
.feature p{font-size:7.5px;line-height:1.5;color:var(--muted);margin-bottom:7px}

/* blog + testimonials */
.lower{position:absolute;top:793px;left:98px;width:572px;display:flex;gap:40px}
.lower section{flex:1}
.lower h5{font-family:"Raleway",sans-serif;font-size:15px;font-weight:700;color:var(--blue);margin-bottom:10px}
.post{margin-bottom:10px}
.post strong{display:block;font-size:8.5px;color:var(--ink);margin-bottom:3px}
.post p{font-size:7.5px;line-height:1.5;color:var(--muted)}
.post a{font-size:7.5px;font-weight:700;color:var(--ink);text-decoration:none}
.testimonial{display:flex;gap:10px;margin-bottom:14px}
.avatar{flex:0 0 34px;height:34px;border-radius:50%;background:radial-gradient(circle at 50% 40%,#c9a68a,#7f6a5c)}
.testimonial p{font-size:7.5px;line-height:1.5;color:var(--muted)}
.testimonial span{display:block;font-size:7.5px;font-weight:700;color:var(--ink);margin-top:3px}

/* footer */
.site-footer{position:absolute;top:1024px;left:0;width:768px;height:176px;background:var(--footer);color:#c9d8da}
.footer-cols{display:flex;padding:22px 98px 0;gap:30px}
.footer-col{flex:1}
.footer-col.wide{flex:1.5}
.footer-col h6{font-family:"Raleway",sans-serif;font-size:13px;font-weight:600;color:var(--white);margin-bottom:8px}
.footer-col li{list-style:none;font-size:7.5px;line-height:1.8}
.social{display:flex;gap:5px;margin-top:6px}
.social span{width:15px;height:15px;border-radius:50%;background:var(--teal)}
.social span:nth-child(2){background:var(--blue)}
.social span:nth-child(3){background:#4a78b5}
.social span:nth-child(4){background:#d2553f}
.copyright{position:absolute;bottom:0;left:0;width:100%;height:30px;background:var(--footer-deep);font-size:7.5px;padding:10px 98px;color:#9fb3b6}
</style>
</head>
<body>

<header class="site-header">
  <div class="brand"><span class="brand-dot"></span>AlpenGlow Deals</div>
  <div class="booking-contact">
    <div class="label">BOOKING NOW</div>
    <div class="phone">
      <svg width="14" height="14" viewBox="0 0 24 24" aria-hidden="true"><path fill="#2fa6bd" d="M6.6 10.8a15.1 15.1 0 0 0 6.6 6.6l2.2-2.2c.3-.3.7-.4 1-.2 1.1.4 2.3.6 3.6.6.6 0 1 .4 1 1V20c0 .6-.4 1-1 1A17 17 0 0 1 3 4c0-.6.4-1 1-1h3.5c.6 0 1 .4 1 1 0 1.3.2 2.5.6 3.6.1.3 0 .7-.2 1z"/></svg>
      555.014.2207
    </div>
  </div>
</header>

<nav class="main-nav">
  <a href="#">HOME</a><a href="#">ABOUT US</a><a href="#">SERVICES</a><a href="#">ROOMS FOR RENT</a><a href="#">PRICES</a><a href="#">GALLERY</a><a href="#">BLOG</a><a href="#">CONTACT</a>
</nav>

<section class="hero" role="img" aria-label="Snowy wooden chalet balcony overlooking a winter ski resort">
  <div class="hero-tagline">
    <h1>Last Minute Accommodation</h1>
    <h2>Booking Portal</h2>
    <p>Find available ski resort rooms and apartments for your last minute winter break.</p>
  </div>
  <form class="booking-form">
    <div class="title">BOOK NOW</div>
    <div class="body">
      <div class="field-label">Check In Date</div>
      <div class="field">
        <svg width="9" height="9" viewBox="0 0 10 10" aria-hidden="true"><rect x=".5" y="1.5" width="9" height="8" fill="none" stroke="#7b8288"/><line x1=".5" y1="4" x2="9.5" y2="4" stroke="#7b8288"/></svg>
        Tue, 17 Dec 2024</div>
      <div class="field-label">Check out Date</div>
      <div class="field">
        <svg width="9" height="9" viewBox="0 0 10 10" aria-hidden="true"><rect x=".5" y="1.5" width="9" height="8" fill="none" stroke="#7b8288"/><line x1=".5" y1="4" x2="9.5" y2="4" stroke="#7b8288"/></svg>
        Fri, 20 Dec 2024</div>
      <div class="selects">
        <div><div class="field-label">Rooms</div><div class="field">01 ▾</div></div>
        <div><div class="field-label">Adults</div><div class="field">02 ▾</div></div>
        <div><div class="field-label">Kids</div><div class="field">00 ▾</div></div>
      </div>
      <div class="check-btn">CHECK AVAILABILITY</div>
    </div>
  </form>
</section>

<section class="welcome">
  <h3 class="heading">Welcome to Our Website Mainpage</h3>
  <p>Browse last minute rooms and apartments offered by local hotel and chalet owners across the valley. Every listing shows clear dates, beds and pricing so you can compare deals quickly and book your winter break with total confidence and no hidden fees.</p>
  <p>Owners can post open dates within two weeks and reach active skiers and snowboarders instantly. Guests can post their own request with dates, number of beds and budget, then receive matching offers straight to their inbox from trusted local hosts.</p>
  <div class="btn-row"><span class="btn">Read More</span><span class="btn">Book Now</span></div>
</section>

<section class="features">
  <article class="feature">
    <div class="feature-photo" role="img" aria-label="Skier carving down a snowy slope" style="background:linear-gradient(160deg,#e8eef3,#9fb4c4 60%,#5b6d7a)"></div>
    <h4>Why Choose Us</h4>
    <p>Local hosts, honest prices and fresh last minute deals updated every day for skiers and mountain lovers.</p>
    <span class="btn">Read More</span>
  </article>
  <article class="feature">
    <div class="feature-photo" role="img" aria-label="Cosy chalet bedroom with wooden walls" style="background:linear-gradient(160deg,#c79a6e,#8a5e3c 60%,#4e3626)"></div>
    <h4>Room for Rent</h4>
    <p>Hotel rooms and apartments near the lifts, listed with dates, beds and clear nightly prices.</p>
    <span class="btn">Read More</span>
  </article>
  <article class="feature">
    <div class="feature-photo" role="img" aria-label="Mountain village covered in snow" style="background:linear-gradient(160deg,#b9cfe0,#eef2f5 50%,#7c8a94)"></div>
    <h4>Services Provides</h4>
    <p>Post a request, get alerts for new offers and manage your bookings from one simple account.</p>
    <span class="btn">Read More</span>
  </article>
</section>

<div class="lower">
  <section>
    <h5>Latest Blog Post</h5>
    <div class="post">
      <strong>Fresh powder this weekend at the resort</strong>
      <p>Snow reports look great for the coming days, so now is the perfect time to grab a late room deal.</p>
      <a href="#">Read More</a>
    </div>
    <div class="post">
      <strong>Planning a short break in the mountains</strong>
      <p>Our quick guide to packing light, picking dates and finding the best value stay at short notice.</p>
      <a href="#">Read More</a>
    </div>
  </section>
  <section>
    <h5>Testimonials</h5>
    <div class="testimonial">
      <div class="avatar" role="img" aria-label="Guest portrait"></div>
      <div><p>We booked a lovely apartment two days before arrival and saved a lot. Friendly hosts and a very easy process.</p><span>By Author Name</span></div>
    </div>
    <div class="testimonial">
      <div class="avatar" role="img" aria-label="Guest portrait"></div>
      <div><p>Listing our empty rooms took minutes and they were filled the same week. A great way to reach skiers quickly.</p><span>By Author Name</span></div>
    </div>
  </section>
</div>

<footer class="site-footer">
  <div class="footer-cols">
    <div class="footer-col"><h6>Company</h6><ul><li>About Us</li><li>Why Choose Us</li><li>Booking Now</li><li>Rooms for Rent</li></ul></div>
    <div class="footer-col"><h6>Resources</h6><ul><li>Testimonials</li><li>Terms &amp; Privacy</li><li>Site Map</li><li>Gallery</li></ul></div>
    <div class="footer-col"><h6>Support</h6><ul><li>Terms of Use</li><li>Contact Us</li><li>Sitemap</li></ul></div>
    <div class="footer-col wide"><h6>Contact Us</h6><ul><li>12 Alpine Road, Snowtown 10245</li><li>555.014.2207</li><li>info@alpenglowdeals.com</li></ul>
      <div class="social"><span></span><span></span><span></span><span></span></div>
    </div>
  </div>
  <div class="copyright">© 2024 AlpenGlow Deals. All rights reserved.</div>
</footer>

</body>
</html>
```